Business Card for Technology Startup

Design a 2-sided business card using the logo provided. We are a digital healthcare platform that provides a mobile app and web UI that helps caregivers, families, and doctors share information and provide better patient outcomes. We use AI and machine learning to help guide patients through their day-to-day life. The final design should communicate stability, peace, comfort, but also align with the image of an AI-driven technology startup.

I'd like the deliverable to by a Photoshop PSD file (with layers) that I can work with in pixlr.com. Should contain the following editable layers:
Name (ex. John Doe)
Title (ex. Founder / CEO)
Email (ex. info@brenvaxa.ai)
Phone (ex. (999) 333-5555)
Website (ex. https://brenvaxa.ai)

```html
<!DOCTYPE html>
<html lang="en">
<head>
<meta charset="utf-8">
<title>Brenvaxa Business Card</title>
<link href="https://fonts.googleapis.com/css2?family=Poppins:wght@400;600&display=swap" rel="stylesheet">
<style>
  :root {
    --backdrop: #2b2c2f;
    --card-light: #ffffff;
    --card-dark: #232326;
    --ink: #111114;
    --muted: #6f7075;
    --cyan: #00c8ee;
    --cyan-deep: #05b2e6;
    --cyan-bright: #12e6f7;
    --white: #ffffff;
  }
  * { box-sizing: border-box; margin: 0; padding: 0; }
  html, body {
    width: 1200px; height: 952px; overflow: hidden;
    background: var(--backdrop);
    font-family: "Poppins", sans-serif;
  }
  .sheet {
    position: relative; width: 1200px; height: 952px;
    display: flex; flex-direction: column; align-items: center; justify-content: center; gap: 60px;
  }
  .card {
    position: relative; width: 640px; height: 366px; overflow: hidden;
    box-shadow: 0 14px 30px rgba(0,0,0,.45);
  }
  .card--front { background: var(--card-light); }
  .card--back { background: var(--card-dark); }

  .brand { display: flex; align-items: center; gap: 12px; font-weight: 600; letter-spacing: .5px; }
  .brand__dot { border-radius: 50%; background: var(--cyan); flex: none; }

  .card--front .brand { position: absolute; left: 42px; top: 40px; color: var(--ink); font-size: 38px; line-height: 1.2; }
  .card--front .brand__dot { width: 22px; height: 22px; }

  .contact { position: absolute; left: 42px; top: 176px; list-style: none; }
  .contact__item { display: flex; align-items: center; gap: 9px; font-size: 13px; line-height: 20px; color: var(--muted); margin-bottom: 7px; white-space: nowrap; }
  .contact__icon { width: 18px; height: 18px; border-radius: 3px; background: var(--ink); display: flex; align-items: center; justify-content: center; flex: none; }
  .contact__icon svg { width: 12px; height: 12px; }

  .person { position: absolute; right: 42px; top: 176px; text-align: right; }
  .person__name { font-size: 27px; line-height: 1.2; font-weight: 600; color: var(--ink); letter-spacing: 1px; }
  .person__title { font-size: 13px; line-height: 1.5; color: var(--muted); }

  .decor {
    position: absolute; left: 300px; bottom: 0; width: 340px; height: 110px;
    border-radius: 60px 0 0 0;
    background: linear-gradient(120deg, var(--cyan-deep), var(--cyan-bright));
  }

  .card--back .brand { position: absolute; left: 0; right: 0; top: 148px; justify-content: center; color: var(--white); font-size: 50px; line-height: 1.2; }
  .card--back .brand__dot { width: 28px; height: 28px; }
  .accent-line { position: absolute; left: 0; right: 0; bottom: 58px; height: 2px; background: var(--cyan); }
</style>
</head>
<body>
<main class="sheet">
  <section class="card card--front" aria-label="Business card front">
    <div class="brand"><span class="brand__dot"></span><span>brenvaxa</span></div>
    <ul class="contact">
      <li class="contact__item">
        <span class="contact__icon"><svg viewBox="0 0 24 24"><path fill="#fff" d="M6.6 10.8a15 15 0 0 0 6.6 6.6l2.2-2.2c.3-.3.7-.4 1-.2 1.1.4 2.3.6 3.6.6.6 0 1 .4 1 1V20c0 .6-.4 1-1 1A17 17 0 0 1 3 4c0-.6.4-1 1-1h3.5c.6 0 1 .4 1 1 0 1.3.2 2.5.6 3.6.1.3 0 .7-.2 1z"/></svg></span>
        555 014-2276
      </li>
      <li class="contact__item">
        <span class="contact__icon"><svg viewBox="0 0 24 24"><rect x="3" y="6" width="18" height="12" fill="none" stroke="#fff" stroke-width="2"/><path d="M3 6l9 7 9-7" fill="none" stroke="#fff" stroke-width="2"/></svg></span>
        info@brenvaxa.ai
      </li>
      <li class="contact__item">
        <span class="contact__icon"><svg viewBox="0 0 24 24"><circle cx="12" cy="12" r="9" fill="none" stroke="#fff" stroke-width="2"/><path d="M3 12h18M12 3c3 3 3 15 0 18M12 3c-3 3-3 15 0 18" fill="none" stroke="#fff" stroke-width="1.6"/></svg></span>
        www.brenvaxa.ai
      </li>
    </ul>
    <div class="person">
      <p class="person__name">JOHN DOE</p>
      <p class="person__title">Founder / CEO</p>
    </div>
    <div class="decor" role="img" aria-label="Cyan brand decoration area"></div>
  </section>

  <section class="card card--back" aria-label="Business card back">
    <div class="brand"><span class="brand__dot"></span><span>brenvaxa</span></div>
    <div class="accent-line"></div>
  </section>
</main>
</body>
</html>
```